Halvern Guildworks Business Cards
Need out-of-the-box business card design
Halvern Guildworks Business Cards -
Creative Brief
Modern
Peter Strandquell
5172 Orrin St. Denver, CO 80219
peter@halvernguildworks.com
halvernguildworks.com
We exist to foster healthy artist Community, create points of Collaboration and provide tangible benefit to local Causes.

```html
<!DOCTYPE html>
<html lang="en">
<head>
<meta charset="utf-8">
<title>Halvern Guildworks Business Cards</title>
<link href="https://fonts.googleapis.com/css2?family=PT+Serif:wght@400;700&display=swap" rel="stylesheet">
<style>
  :root {
    --backdrop: #ece8df;
    --card-white: #ffffff;
    --gold: #b0922f;
    --gold-deep: #94781f;
    --leaf: #6f8b2a;
    --gold-text: #a4862a;
    --ink: #4a4026;
    --paper-text: #ffffff;
  }
  * { margin: 0; padding: 0; box-sizing: border-box; }
  html, body {
    width: 1200px; height: 852px; overflow: hidden;
    background: var(--backdrop);
    font-family: "PT Serif", Georgia, serif;
  }
  .canvas { position: relative; width: 1200px; height: 852px; }
  .card {
    position: absolute; width: 520px; height: 300px;
    border-radius: 14px; overflow: hidden;
    background: var(--card-white);
    box-shadow: 0 6px 18px rgba(60, 45, 20, 0.18);
  }
  .card--front { left: 80px; top: 110px; }
  .card--back { left: 600px; top: 440px; }
  .card-shape { position: absolute; inset: 0; width: 100%; height: 100%; }
  .brand {
    position: absolute; display: flex; align-items: center; gap: 12px;
    color: var(--leaf); font-weight: 400; font-size: 30px; line-height: 1;
  }
  .brand-dot { width: 26px; height: 26px; border-radius: 50%; background: var(--gold); flex: none; }
  .person-name {
    position: absolute; color: var(--gold-text);
    font-weight: 700; font-size: 16px;
  }
  .contact {
    position: absolute; right: 30px; text-align: right;
    font-size: 11.5px; line-height: 1.45;
  }
  .contact-row { display: flex; justify-content: flex-end; align-items: center; gap: 7px; }
  .contact-icon { width: 11px; height: 11px; flex: none; }
  .card--front .address { color: var(--ink); }
  .card--front .on-gold { color: var(--paper-text); }
  .card--back .contact { color: var(--ink); }
</style>
</head>
<body>
<main class="canvas">

  <section class="card card--front" aria-label="Business card, front">
    <svg class="card-shape" viewBox="0 0 520 300" preserveAspectRatio="none" aria-hidden="true">
      <path d="M0,300 L0,262 C170,246 330,190 410,90 C445,44 480,14 520,4 L520,300 Z" fill="var(--gold)"/>
      <path d="M0,254 C170,238 325,182 402,84 C438,38 476,8 520,-2" fill="none" stroke="var(--leaf)" stroke-width="5"/>
    </svg>
    <div class="brand" style="left:38px; top:70px;">
      <span class="brand-dot"></span>Halvern Guildworks
    </div>
    <div class="person-name" style="left:88px; top:145px;">Peter Strandquell</div>
    <div class="contact address" style="top:118px;">
      <div>5172 Orrin St.</div>
      <div>Denver, CO 80219</div>
    </div>
    <div class="contact on-gold" style="top:168px;">
      <div class="contact-row">3035550148
        <svg class="contact-icon" viewBox="0 0 12 12"><path d="M3,1 C1,2 1,5 4,8 C7,11 10,11 11,9 L9,7 L7.5,8 C6,7 5,6 4,4.5 L5,3 Z" fill="#fff"/></svg>
      </div>
      <div class="contact-row">peter@halvernguildworks.com
        <svg class="contact-icon" viewBox="0 0 12 12"><rect x="1" y="2.5" width="10" height="7" rx="1" fill="#fff"/><path d="M1.5,3 L6,6.5 L10.5,3" fill="none" stroke="var(--gold)" stroke-width="1"/></svg>
      </div>
      <div class="contact-row">halvernguildworks.com
        <svg class="contact-icon" viewBox="0 0 12 12"><circle cx="6" cy="6" r="5" fill="none" stroke="#fff" stroke-width="1.2"/><path d="M1,6 H11 M6,1 C3,4 3,8 6,11 M6,1 C9,4 9,8 6,11" fill="none" stroke="#fff" stroke-width="0.9"/></svg>
      </div>
    </div>
  </section>

  <section class="card card--back" aria-label="Business card, back">
    <svg class="card-shape" viewBox="0 0 520 300" preserveAspectRatio="none" aria-hidden="true">
      <path d="M0,178 C150,196 330,236 470,300 L0,300 Z" fill="var(--gold)"/>
      <path d="M0,170 C150,188 335,228 482,300" fill="none" stroke="var(--leaf)" stroke-width="4"/>
    </svg>
    <div class="person-name" style="right:30px; top:28px;">Peter Strandquell</div>
    <div class="brand" style="left:38px; top:108px;">
      <span class="brand-dot"></span>Halvern Guildworks
    </div>
    <div class="contact" style="top:92px;">
      <div>5172 Orrin St.</div>
      <div>Denver, CO 80219</div>
      <div class="contact-row" style="margin-top:10px;">3035550148
        <svg class="contact-icon" viewBox="0 0 12 12"><path d="M3,1 C1,2 1,5 4,8 C7,11 10,11 11,9 L9,7 L7.5,8 C6,7 5,6 4,4.5 L5,3 Z" fill="var(--gold)"/></svg>
      </div>
      <div class="contact-row">peter@halvernguildworks.com
        <svg class="contact-icon" viewBox="0 0 12 12"><rect x="1" y="2.5" width="10" height="7" rx="1" fill="var(--gold)"/><path d="M1.5,3 L6,6.5 L10.5,3" fill="none" stroke="#fff" stroke-width="1"/></svg>
      </div>
      <div class="contact-row">halvernguildworks.com
        <svg class="contact-icon" viewBox="0 0 12 12"><circle cx="6" cy="6" r="5" fill="none" stroke="var(--gold)" stroke-width="1.2"/><path d="M1,6 H11 M6,1 C3,4 3,8 6,11 M6,1 C9,4 9,8 6,11" fill="none" stroke="var(--gold)" stroke-width="0.9"/></svg>
      </div>
    </div>
  </section>

</main>
</body>
</html>
```